Varimel Sciences needs high end Label Design for a revolutionary new supplement

We at Varimel Sciences are looking for a brand new Label Design for a first of its kind product called Morivane. It is the first supplement on the market that treats grief and heartbreak. This product is unisex for both men and woman. We want the New Label to look high end and luxurious using the brand colors which are gold and burgundy. Please feel free to use other colors such as black, white, or gray to go along with it or any other colors if you feel would be a great fit! Varimel Sciences is like the Zephlon of the supplement world, coming out with new products that will challenge the way people treat different symptoms. To Recap:

1. Product Name: MORIVANE - the font will play a big roll
2. The Label will be placed on an all white bottle
3. Some parts of the label will be printed with foil to make parts of the label shiny and more attractive. Please keep this in mind when designing.
4. Must use our Logo. I will attach a file of our logo and of the emblem as well. Feel free to use the emblem separately if you have a great idea for it. Please let us know if you need the Logo in a different file type.
5. This all natural herbal supplement in pill form is the first to treat grief and support someone with a broken heart. The consumers purchasing this product will be going through a hard and emotional time. This is a serious product.
6. The manufacturer has included some basic instructions regarding the dye line and file types. Please do your best to meet these. If you cannot meet the guidelines please submit art work anyways. If your design is chosen we will just have the manufacturer replicate the design.

The final label should portray Morivane and Varimel Sciences as a luxurious brand and product which was made with cutting edge science leading the way with revolutionary ideas. We want customers to feel that the product is worth every penny, because it is. As soon as they receive the product and take one look at the label, I want them to think WOW I made the right choice buying this. I have attached some Label designs that we really liked for your review.

Please feel free to message me with any questions or if you need the Logo in a different file type. Thank you all.
Updates

Please send in more entries while we take a couple days to review, we are still looking for that one design we can work with. We are getting close, thank you all!

Target Market(s)

People going through grief and heartbreak.

Font styles to use
Sans Serif
Script
Other font styles liked:
• Any font that looks good, The font for the name MORIVANE is very important and will brand it. We hated the font used in the label we received in our first label draft (attached so you can see)

Requirements
Must have
• Must have the company Logo that says the company name
• Must have the colors Gold and Burgundy
• Must have some areas that will be the shiny foil when label is printed.
• Must say "Dietary Supplement" somewhere near the bottom along with "90 Capsules"
• I have attached a Label someone designed for us but were not really happy with. I did like the font the "Dietary supplement" and "90 Capsules" had and also where it was placed. We absolutely HATED the font used for Morivane.
• Must look at the label design we received from the manufacturer and take into consideration the room needed to write in the directions and all the symbols such as "made in america" and "QPA Facility" Don't worry about adding these in as they will put those in before printing but keep in mind they will be added to the Final Label along with the Supplement Facts.
Nice to have
• Would like to see other colors to go with gold and burgundy suck as black, white, or gray. I have attached some Label designs that I really liked for your reference.
Should not have
• Does not need to have any other legal language, that will be applied by the the manufacturer's graphics team.

```html
<!DOCTYPE html>
<html lang="en">
<head>
<meta charset="utf-8">
<title>Morivane Label – Varimel Sciences</title>
<link rel="stylesheet" href="https://fonts.googleapis.com/css2?family=Cinzel:wght@600&family=Lato:wght@400;700&family=Roboto:wght@400;500;700&family=Russo+One&display=swap">
<style>
  :root {
    --backdrop: #808186;
    --burgundy: #5b0f13;
    --burgundy-deep: #3a080b;
    --burgundy-ink: #6e1116;
    --gold: #d6a23f;
    --gold-light: #e6c05a;
    --gold-dark: #7b4a1b;
    --accent-red: #b3212c;
    --white: #f7f7f8;
  }
  * { box-sizing: border-box; margin: 0; padding: 0; }
  html, body { width: 1200px; height: 572px; overflow: hidden; }
  body { background: var(--backdrop); position: relative; font-family: "Lato", sans-serif; }

  .label {
    position: absolute; left: 120px; top: 94px; width: 1092px; height: 384px;
    background: radial-gradient(ellipse at 50% 50%, var(--burgundy) 0%, var(--burgundy-deep) 100%);
    box-shadow: 0 6px 14px rgba(0,0,0,.35);
    overflow: hidden;
  }
  .foil-band {
    position: absolute; left: 0; width: 100%; height: 26px;
    background: linear-gradient(90deg, var(--gold-dark), #b98a36 20%, var(--gold-light) 45%, #b98a36 70%, var(--gold-dark));
  }
  .foil-band--top { top: 0; border-bottom: 3px solid var(--accent-red); }
  .foil-band--bottom { bottom: 0; border-top: 3px solid var(--accent-red); }

  .center-panel { position: absolute; left: 0; top: 0; }

  .info-column {
    position: absolute; left: 22px; top: 46px; width: 240px;
    color: var(--gold); font-size: 8.2px; line-height: 1.25;
  }
  .info-column p { margin-bottom: 8px; }
  .info-column strong { font-weight: 700; }
  .precautions { margin-top: 14px; text-transform: uppercase; }

  .badge-row { position: absolute; left: 22px; top: 222px; display: flex; gap: 9px; }
  .badge { width: 40px; text-align: center; color: var(--gold); font-size: 7.6px; }
  .badge-mark {
    width: 28px; height: 28px; margin: 0 auto 5px; border-radius: 50%;
    border: 2px solid var(--gold); background: rgba(214,162,63,.15);
  }

  .batch-dates {
    position: absolute; left: 178px; top: 292px; color: var(--gold);
    font-family: "Roboto", sans-serif; font-size: 9.5px; line-height: 1.4;
  }

  .brand { position: absolute; left: 330px; top: 58px; width: 300px; text-align: center; }
  .brand-dot { width: 34px; height: 34px; border-radius: 50%; background: var(--accent-red); margin: 0 auto 10px; }
  .brand-name {
    font-family: "Cinzel", serif; font-weight: 600; color: var(--accent-red);
    font-size: 23px; letter-spacing: 2px; line-height: 1.05;
  }

  .product-name {
    position: absolute; left: 280px; top: 196px; width: 400px; text-align: center;
    font-family: "Russo One", sans-serif; font-size: 50px; color: var(--burgundy-ink);
    letter-spacing: 1px;
  }

  .pack-info {
    position: absolute; left: 380px; top: 285px; width: 200px; text-align: center;
    font-family: "Lato", sans-serif; font-weight: 700; color: var(--burgundy-deep);
    font-size: 15px; line-height: 1.3;
    border-left: 3px solid var(--burgundy-deep); border-right: 3px solid var(--burgundy-deep);
    padding: 6px 0;
  }
  .pack-info::before, .pack-info::after {
    content: ""; position: absolute; left: 0; right: 0; height: 3px;
    background: linear-gradient(90deg, var(--burgundy-deep) 10%, transparent 10%, transparent 90%, var(--burgundy-deep) 90%);
  }
  .pack-info::before { top: 0; }
  .pack-info::after { bottom: 0; }

  .facts-panel {
    position: absolute; left: 690px; top: 48px; width: 252px;
    border: 2px solid var(--gold); padding: 3px 6px 2px;
    color: var(--gold); font-family: "Roboto", sans-serif;
  }
  .facts-title { font-size: 21px; font-weight: 700; line-height: 1.1; }
  .facts-serving { font-size: 11px; font-weight: 500; padding-bottom: 3px; border-bottom: 6px solid var(--gold); }
  .facts-head {
    display: flex; justify-content: space-between; font-size: 10px; font-weight: 700;
    padding: 3px 0; border-bottom: 2px solid var(--gold);
  }
  .facts-row { display: flex; font-size: 9.6px; padding: 4px 0 4px 2px; border-bottom: 1px solid var(--gold); line-height: 1.3; }
  .facts-row .ingredient { flex: 1; }
  .facts-row .amount { width: 48px; }
  .facts-row .dv { width: 14px; text-align: right; }
  .indent { padding-left: 12px; }
  .facts-row:last-of-type { border-bottom: 6px solid var(--gold); }
  .facts-note { font-size: 9px; padding: 3px 0 1px; }

  .other-ingredients {
    position: absolute; left: 692px; top: 226px; width: 260px;
    color: var(--gold); font-family: "Roboto", sans-serif; font-size: 9.4px; line-height: 1.35;
  }
  .other-ingredients p + p { margin-top: 4px; text-transform: uppercase; font-size: 9.8px; }

  .distributor {
    position: absolute; left: 692px; top: 300px; color: var(--gold);
    font-family: "Roboto", sans-serif; font-weight: 700; font-size: 15.5px; line-height: 1.4;
  }
</style>
</head>
<body>
  <section class="label">
    <svg class="center-panel" width="1092" height="384" viewBox="0 0 1092 384" aria-hidden="true">
      <path d="M248 120 C 120 360 260 430 220 384" fill="none" stroke="rgba(0,0,0,.18)" stroke-width="18"/>
      <path d="M340 26 C 255 110 262 300 305 358 L 655 358 C 722 250 705 90 640 26 Z" fill="var(--white)"/>
    </svg>

    <div class="foil-band foil-band--top"></div>
    <div class="foil-band foil-band--bottom"></div>

    <div class="info-column">
      <p><strong>Direction:</strong> Adult take 2 Capsules daily, as a dietary supplement. Or as directed by a he practitioner</p>
      <p><strong>Benefits:</strong> Promote fat burning, help to control the weight.</p>
      <p><strong>Warnings:</strong> If you are pergnant or breastfeeding, persons under the age of 18, consult a doctor before use. Do not use if you are hypersensitivity to any of the formula ingredients.</p>
      <p><strong>Storage Condition:</strong> Keep container tightly sealed in a cool and dry place. Avoide heat and light.</p>
      <p class="precautions">Precautions:<br>Do not use this product if safety seal is missing or broken keep out of reach of children.</p>
    </div>

    <div class="badge-row">
      <div class="badge"><div class="badge-mark"></div>Cruelty Free</div>
      <div class="badge"><div class="badge-mark"></div>Sugar Free</div>
      <div class="badge"><div class="badge-mark"></div>Dairy Free</div>
      <div class="badge"><div class="badge-mark"></div>Gluten Free</div>
      <div class="badge"><div class="badge-mark"></div>Non GMO</div>
    </div>

    <div class="batch-dates">
      Manufacturing:<br>00 / 00 /00<br>Expiry date:<br>00 / 00 /00
    </div>

    <div class="brand">
      <div class="brand-dot"></div>
      <div class="brand-name">VARIMEL<br>SCIENCES</div>
    </div>

    <h1 class="product-name">MORIVANE</h1>

    <div class="pack-info">90 Capsules<br>Dietary Supplement</div>

    <div class="facts-panel">
      <div class="facts-title">Supplement Facts</div>
      <div class="facts-serving">Serving Size 1 Capsule</div>
      <div class="facts-head"><span>Amount Per Serving</span><span>% DV</span></div>
      <div class="facts-row">
        <span class="ingredient">Milk Thistle Seed Extract<br><span class="indent">standardized to 80% silymarin</span><br>(140 mg)</span>
        <span class="amount">175 mg</span><span class="dv">**</span>
      </div>
      <div class="facts-row">
        <span class="ingredient">Blessed Thistle (stem. leaf, Flower)</span>
        <span class="amount">120 mg</span><span class="dv">**</span>
      </div>
      <div class="facts-note">**Daily Value (DV) not established.</div>
    </div>

    <div class="other-ingredients">
      <p>Other Ingredients: plant-derived capsule (hypromellose), Cellulose</p>
      <p>Gluten-free, sugar-free, no preservatives added, no artificial flavor</p>
    </div>

    <div class="distributor">Distributed by:<br>Varimel Sciences, LLC</div>
  </section>
</body>
</html>
```